Simple Business Cards for Self-employed Coach

Simple business card with a design that includes the QLT logo.
Using either only the logo color or additional colors that match the logo.

Meridian Guides reach deeply into the past, gathering wisdom from East and West, while still staying current with the frontiers of new discovery in cognitive science, genetics, and other disciplines. see https://www.brightharborpath.example/what-is-integral-coaching/

Target Market(s)

Coaching Clients in Tokyo /Asia; in business organizations, but also outside

Industry/Entity Type

Life Coaching

Contact Information for Business Card

Lukas Brenning
Certified Meridian Guide

3-2-48 Kamiyoshi
Nakarino 164-0392
Tokyo, Japan

Phone: +81 70 4817 5062
E-Mail: lukas.brenning@mailora.example

Font styles to use
Sans Serif

Colors
00a990

Requirements
Must have
• include uploaded logo
• color fitting with QLT logo color
Nice to have
• simple, elegant design
Should not have
• clutter

```html
<!DOCTYPE html>
<html lang="en">
<head>
<meta charset="utf-8">
<title>QLT Business Card</title>
<link href="https://fonts.googleapis.com/css2?family=Open+Sans:wght@400;600;700&display=swap" rel="stylesheet">
<style>
  :root {
    --brand: #00a990;
    --brand-bright: #12c3a3;
    --brand-soft: #6fd3c0;
    --paper: #ffffff;
    --backdrop: #e4e5e7;
    --ink-muted: #5fbfae;
  }
  * { box-sizing: border-box; margin: 0; padding: 0; }
  html, body {
    width: 1200px; height: 800px; overflow: hidden;
    background: var(--backdrop);
    font-family: "Open Sans", Arial, sans-serif;
  }
  .canvas {
    width: 1200px; height: 800px;
    display: flex; align-items: center; justify-content: center; gap: 40px;
  }
  .card {
    position: relative; width: 540px; height: 309px; overflow: hidden;
    box-shadow: 0 10px 28px rgba(0,0,0,0.12);
  }

  /* Logo side */
  .card--brand { background: var(--brand-bright); }
  .card--brand .facets { position: absolute; inset: 0; }
  .brand-mark {
    position: absolute; left: 50%; top: 50%; transform: translate(-50%, -50%);
    display: flex; align-items: center; gap: 18px;
  }
  .brand-mark__name {
    color: var(--paper); font-weight: 700; font-size: 64px; letter-spacing: 14px;
  }
  .brand-mark__dot {
    width: 34px; height: 34px; border-radius: 50%; background: var(--paper);
  }

  /* Contact side */
  .card--contact { background: var(--paper); }
  .card--contact .edge {
    position: absolute; left: 0; top: 0; bottom: 0; width: 16px; background: var(--brand-bright);
  }
  .card--contact .corner { position: absolute; inset: 0; }
  .corner-mark {
    position: absolute; right: 38px; top: 148px;
    color: var(--paper); font-weight: 700; font-size: 30px; letter-spacing: 6px;
    display: flex; align-items: center; gap: 10px;
  }
  .corner-mark__dot { width: 14px; height: 14px; border-radius: 50%; background: var(--paper); }

  .contact { position: absolute; left: 48px; top: 30px; color: var(--brand); }
  .contact .icon { width: 14px; height: 14px; fill: var(--brand); display: block; }
  .person__name { font-weight: 600; font-size: 21px; line-height: 1.2; margin-top: 4px; }
  .person__title { font-size: 19px; color: var(--brand-soft); line-height: 1.2; }
  .address { margin-top: 16px; font-size: 11px; line-height: 1.35; color: var(--ink-muted); }
  .address .icon { margin-bottom: 4px; }
  .address__city { font-weight: 700; color: var(--brand); }
  .divider { width: 50px; height: 1px; background: #e3f3ef; margin: 10px 0 12px; }
  .reach { font-size: 16px; line-height: 1.45; }
  .reach__row { display: flex; align-items: center; gap: 8px; }
  .reach__at { font-size: 16px; width: 14px; text-align: center; }
</style>
</head>
<body>
<main class="canvas">

  <section class="card card--brand" aria-label="Business card, logo side">
    <svg class="facets" viewBox="0 0 540 309" preserveAspectRatio="none" aria-hidden="true">
      <polygon points="0,0 260,0 120,309 0,309" fill="#0aa88f" opacity="0.55"/>
      <polygon points="0,160 540,250 540,309 0,309" fill="#0fb396" opacity="0.45"/>
      <polygon points="300,0 540,0 540,120" fill="#1ccbab" opacity="0.5"/>
    </svg>
    <div class="brand-mark">
      <span class="brand-mark__name">QLT</span>
      <span class="brand-mark__dot"></span>
    </div>
  </section>

  <section class="card card--contact" aria-label="Business card, contact side">
    <div class="edge"></div>
    <svg class="corner" viewBox="0 0 540 309" preserveAspectRatio="none" aria-hidden="true">
      <polygon points="400,110 540,110 540,250 375,250" fill="var(--brand-bright)"/>
    </svg>
    <div class="corner-mark">
      <span>QLT</span><span class="corner-mark__dot"></span>
    </div>

    <div class="contact">
      <svg class="icon" viewBox="0 0 16 16" aria-hidden="true"><circle cx="8" cy="5" r="3.5"/><path d="M1 16c0-4 3-6 7-6s7 2 7 6z"/></svg>
      <p class="person__name">Lukas Brenning</p>
      <p class="person__title">Certified Meridian Guide</p>

      <div class="address">
        <svg class="icon" viewBox="0 0 16 16" aria-hidden="true"><path d="M8 0a5.5 5.5 0 0 0-5.5 5.5C2.5 10 8 16 8 16s5.5-6 5.5-10.5A5.5 5.5 0 0 0 8 0zm0 8a2.5 2.5 0 1 1 0-5 2.5 2.5 0 0 1 0 5z"/></svg>
        <p>3-2-48 Kamiyoshi</p>
        <p>Nakarino 164-0392</p>
        <p class="address__city">Tokyo, Japan</p>
      </div>
      <div class="divider"></div>

      <div class="reach">
        <p class="reach__row">
          <svg class="icon" viewBox="0 0 16 16" aria-hidden="true"><path d="M3.6 1l2.2 3.1-1.3 1.6c.9 2 2.6 3.7 4.6 4.6l1.6-1.3L13.8 11l-1.2 3.4C6.5 14.4 1.6 9.5 1.6 3.4z"/></svg>
          +81 70 4817 5062
        </p>
        <p class="reach__row"><span class="reach__at">@</span>lukas.brenning@mailora.example</p>
      </div>
    </div>
  </section>

</main>
</body>
</html>
```